Infographic for B2B Service solution offering (sales funnel)

Attached is an example of something we need assistance with making into a more professional infographic. These infographics are for our B2B marketing services, aimed at IT Consulting firms.

We have done some basic graphics (attached) and this will provide you guidance (video link on google sheet):
https://files.plonkaret.com/doc/7kQm2Rvx9TbLw4PzHn3YcJa8EuVd6SgFi1MoXp5Ct/view?mode=share

Here are some examples you can model for the new infographic:
https://store.vendrilo.net/box/folders/84TpKwa3Mz9Rj2Lbn6Yq-Hfx5CeGsv?ref=box_link

Target Market(s)

B2B IT Consulting Firms

Industry/Entity Type

Information Technology, Consulting

Colors

Designer to choose colors to be used in the design.

Requirements
Must have
• professional, high level consulting firms are target market
Should not have
• cartoonish

```html
<!DOCTYPE html>
<html lang="en">
<head>
<meta charset="utf-8">
<title>Creating B2B Relationships: The Lift IT Trust Building Offers Method</title>
<link rel="stylesheet" href="https://fonts.googleapis.com/css2?family=Catamaran:wght@600;700&family=League+Spartan:wght@700;800&display=swap">
<style>
  :root {
    --paper: #f1f1ef;
    --ink: #000000;
    --white: #ffffff;
    --stage-a: #eb6632;
    --stage-b: #f5a71a;
    --stage-c: #83bd41;
    --stage-d: #1ab4a9;
    --stage-e: #4177bb;
    --stage-f: #645a8f;
    --stage-g: #9b437e;
    --trust-low: #d94848;
    --trust-mid: #f2e21a;
    --trust-high: #86bf3e;
  }
  html, body {
    margin: 0;
    padding: 0;
    width: 1200px;
    height: 1200px;
    overflow: hidden;
    background: var(--paper);
  }
  .infographic {
    display: block;
    width: 1200px;
    height: 1200px;
  }
  .title-text {
    font-family: "Catamaran", sans-serif;
    font-weight: 700;
    fill: var(--white);
  }
  .heading {
    font-family: "League Spartan", sans-serif;
    font-weight: 800;
    font-size: 52px;
    fill: var(--ink);
  }
  .stage-label, .cold-leads {
    font-family: "League Spartan", sans-serif;
    font-weight: 800;
    fill: var(--ink);
  }
  .stage-letter {
    font-family: "League Spartan", sans-serif;
    font-weight: 800;
    font-size: 50px;
    fill: var(--white);
  }
  .leader {
    stroke: var(--ink);
    stroke-width: 1.5;
    fill: none;
  }
  .divider {
    stroke: var(--ink);
    stroke-width: 1.2;
  }
  .funnel {
    filter: drop-shadow(10px 6px 6px rgba(0, 0, 0, 0.18));
  }
  .funnel-outline {
    fill: none;
    stroke: var(--ink);
    stroke-width: 1.8;
    stroke-linejoin: miter;
  }
  .referral-text {
    font-family: "Catamaran", sans-serif;
    font-weight: 700;
    font-size: 26px;
    fill: var(--white);
  }
  .trust-label {
    font-family: "Catamaran", sans-serif;
    font-weight: 700;
    font-size: 31px;
  }
  .trust-low { fill: var(--trust-low); }
  .trust-high { fill: var(--trust-high); }
</style>
</head>
<body>
<svg class="infographic" viewBox="0 0 1200 1200" xmlns="http://www.w3.org/2000/svg">
  <defs>
    <linearGradient id="trust-scale" x1="0" y1="0" x2="0" y2="1">
      <stop offset="0" stop-color="var(--trust-low)"/>
      <stop offset="0.35" stop-color="var(--trust-low)"/>
      <stop offset="0.45" stop-color="#e9893a"/>
      <stop offset="0.56" stop-color="var(--trust-mid)"/>
      <stop offset="0.7" stop-color="var(--trust-high)"/>
      <stop offset="1" stop-color="var(--trust-high)"/>
    </linearGradient>
  </defs>

  <!-- Title banner -->
  <g class="title-banner">
    <path d="M156 178 V76 Q156 38.5 193 38.5 H1013 Q1050 38.5 1050 76 V178 Z" fill="var(--ink)"/>
    <text class="title-text" x="603" y="90" text-anchor="middle" font-size="37">Creating B2B Relationships:</text>
    <text class="title-text" x="603" y="139" text-anchor="middle" font-size="41">The Lift IT “Trust Building Offers” Method</text>
  </g>

  <text class="heading" x="603" y="261" text-anchor="middle" textLength="870">HOW B2B RELATIONSHIPS ARE BUILT</text>

  <!-- Cold leads path to referral -->
  <g class="cold-leads-route">
    <text class="cold-leads" x="486" y="329" font-size="43" textLength="232">COLD LEADS</text>
    <circle cx="748" cy="312" r="7.5" fill="var(--ink)"/>
    <path class="leader" d="M748 312 H889 Q909 312 909 332 V752 Q909 776 890 781"/>
  </g>

  <!-- Funnel -->
  <g class="funnel">
    <polygon points="331,390 876,390 794,520 412,520" fill="var(--stage-a)"/>
    <polygon points="412,520 794,520 730,622 476,622" fill="var(--stage-b)"/>
    <polygon points="476,622 730,622 667,722 539,722" fill="var(--stage-c)"/>
    <polygon points="539,722 667,722 655,742 655,822 551,822 551,742" fill="var(--stage-d)"/>
    <rect x="551" y="822" width="104" height="102" fill="var(--stage-e)"/>
    <rect x="551" y="924" width="104" height="103" fill="var(--stage-f)"/>
    <polygon points="551,1027 655,1027 655,1130 551,1054" fill="var(--stage-g)"/>
    <path class="funnel-outline" d="M331 390 H876 L655 742 V1130 L551 1054 V742 Z"/>
  </g>

  <!-- Stage dividers -->
  <g class="dividers">
    <line class="divider" x1="375" y1="520" x2="831" y2="520"/>
    <line class="divider" x1="430" y1="622" x2="775" y2="622"/>
    <line class="divider" x1="504" y1="722" x2="701" y2="722"/>
    <line class="divider" x1="534" y1="822" x2="671" y2="822"/>
    <line class="divider" x1="534" y1="924" x2="671" y2="924"/>
    <line class="divider" x1="534" y1="1027" x2="671" y2="1027"/>
  </g>

  <!-- Stages -->
  <g class="stage">
    <circle cx="68" cy="475" r="40.5" fill="var(--stage-a)"/>
    <text class="stage-letter" x="68" y="493" text-anchor="middle">A</text>
    <text class="stage-label" x="120" y="469" font-size="32">RESPONSE</text>
    <line class="leader" x1="108" y1="475" x2="470" y2="475"/>
    <circle cx="470" cy="475" r="7.5" fill="var(--ink)"/>
  </g>
  <g class="stage">
    <circle cx="70" cy="571" r="40.5" fill="var(--stage-b)"/>
    <text class="stage-letter" x="72" y="589" text-anchor="middle">B</text>
    <text class="stage-label" x="124" y="566" font-size="32">FIRST CONVERSATION</text>
    <line class="leader" x1="110" y1="571" x2="516" y2="571"/>
    <circle cx="516" cy="571" r="7.5" fill="var(--ink)"/>
  </g>
  <g class="stage">
    <circle cx="70" cy="673" r="40.5" fill="var(--stage-c)"/>
    <text class="stage-letter" x="71" y="691" text-anchor="middle">C</text>
    <text class="stage-label" x="122" y="667" font-size="32">TRUST BUILDING</text>
    <line class="leader" x1="110" y1="673" x2="561" y2="673"/>
    <circle cx="561" cy="673" r="7.5" fill="var(--ink)"/>
  </g>
  <g class="stage">
    <circle cx="70" cy="774" r="40.5" fill="var(--stage-d)"/>
    <text class="stage-letter" x="72" y="792" text-anchor="middle">D</text>
    <text class="stage-label" x="124" y="769" font-size="32">PROBLEM AWARE</text>
    <line class="leader" x1="110" y1="774" x2="603" y2="774"/>
    <circle cx="603" cy="774" r="7.5" fill="var(--ink)"/>
  </g>
  <g class="stage">
    <circle cx="70" cy="873" r="40.5" fill="var(--stage-e)"/>
    <text class="stage-letter" x="70" y="891" text-anchor="middle">E</text>
    <text class="stage-label" x="122" y="869" font-size="32">INTENT</text>
    <line class="leader" x1="110" y1="875" x2="602" y2="875"/>
    <circle cx="602" cy="875" r="7.5" fill="var(--ink)"/>
  </g>
  <g class="stage">
    <circle cx="70" cy="969" r="40.5" fill="var(--stage-f)"/>
    <text class="stage-letter" x="70" y="987" text-anchor="middle">F</text>
    <text class="stage-label" x="124" y="965" font-size="32">CUSTOMER</text>
    <line class="leader" x1="110" y1="971" x2="602" y2="971"/>
    <circle cx="602" cy="971" r="7.5" fill="var(--ink)"/>
  </g>
  <g class="stage">
    <circle cx="70" cy="1066" r="40.5" fill="var(--stage-g)"/>
    <text class="stage-letter" x="69" y="1084" text-anchor="middle">G</text>
    <text class="stage-label" x="124" y="1059" font-size="32">WIFE</text>
    <line class="leader" x1="110" y1="1065" x2="602" y2="1065"/>
    <circle cx="602" cy="1065" r="7.5" fill="var(--ink)"/>
  </g>

  <!-- Referral prospect tag -->
  <g class="referral-tag">
    <line class="leader" x1="640" y1="781" x2="666" y2="781"/>
    <circle cx="640" cy="781" r="7.5" fill="var(--ink)"/>
    <rect x="665" y="762" width="229" height="39" rx="8" fill="var(--ink)"/>
    <text class="referral-text" x="779" y="791" text-anchor="middle">Referral Prospect</text>
  </g>

  <!-- Trust scale -->
  <g class="trust-scale">
    <text class="trust-label trust-low" x="1029" y="416" text-anchor="middle">Low Trust</text>
    <rect x="1027.5" y="432" width="3" height="596" fill="url(#trust-scale)"/>
    <circle cx="1029" cy="432" r="7.5" fill="var(--trust-low)"/>
    <circle cx="1029" cy="1028" r="7.5" fill="var(--trust-high)"/>
    <text class="trust-label trust-high" x="1029" y="1069" text-anchor="middle">High Trust</text>
  </g>
</svg>
</body>
</html>
```